Premium website for 'Kestrel Voyages Elite'

Exclusive Torque League travel packages: world-class tickets, premium hospitality, seamless travel, and curated experiences that bring the spirit of each destination to life.

1. Overall Style and Impression
Aesthetic: Modern, premium, and dynamic, reflecting the speed and excitement of a high-profile sport or event.

Focus: Highly visual and focused on driving users toward specific, high-value conversion points (like finding a race or viewing a premium package).

We need on the homepage a few blocks for all destinations.
One the specific page of the destination, we need a list of tickets.
An example for our website is https://zomerratours.com/

Functional requirements

The web site is designed to deliver an end-to-end Torque League travel experience, combining flight bookings, hotel reservations, and race ticket purchases into one seamless booking process. This system provides a unified API layer that integrates external booking services and enables developers to build, manage, and customize complete travel packages for each TL Grand Prix event.

System Overview

The platform is built around three core microservices, all connected through a central Package API:

1. Flight Booking Service ✈️
Integrates with global flight providers (e.g.,Flyvora API).

2. Hotel Booking Service 🏨
Connects to hotel aggregator APIs (e.g., Bunkly).
Offers real-time availability, dynamic pricing, and filtering by proximity to TL circuits.

3. Ticket Booking Service 🎟️
Manages TL race ticket inventory and seat categories (Grandstand, VIP, General Admission).

CUSTOMER FEEDBACK
After each booking, a customer will be asked to fill in a questionaire.

CHAT BOT
A chat bot will answer the frequently asked questions.

OUR VISION
We believe life is meant to be lived at full throttle.
Not just seen, but felt. Not just remembered, but relived again and again.

MISSION
That’s why we craft once-in-a-lifetime Torque League journeys — where the roar of the engines meets the soul of the city. Where luxury travel and local culture collide with pure adrenaline. Where you don’t just watch the race… you become part of its story.

PRODUCTS

Target Market(s)

Affluent individuals, typically 35−65 years old, in professional, executive, or entrepreneurial roles. High net worth with significant disposable income.

Coding

Coded - Design and coding required

Number of Pages Required

5+ page

Requirements
Must have
• Central Package API
Nice to have
• Customer feedback after each booking , chat bot.

```html
<!DOCTYPE html>
<html lang="en">
<head>
<meta charset="utf-8">
<title>Kestrel Voyages Elite</title>
<link href="https://fonts.googleapis.com/css2?family=Poppins:wght@400;500;600;700&display=swap" rel="stylesheet">
<style>
:root{
  --red:#e31e24;
  --black:#0b0b0b;
  --ink:#1c1c1c;
  --muted:#6b6b6b;
  --line:#dcdcdc;
  --soft:#f1f1f1;
  --white:#ffffff;
}
*{box-sizing:border-box;margin:0;padding:0}
html,body{width:1200px;height:4963px;overflow:hidden}
body{font-family:"Poppins",sans-serif;color:var(--ink);background:var(--white);position:relative}
a{color:inherit;text-decoration:none}
.btn{display:inline-flex;align-items:center;justify-content:center;gap:10px;background:var(--red);color:var(--white);font-size:13px;font-weight:500;text-transform:uppercase;letter-spacing:.3px}
.section-title{position:absolute;left:0;width:1200px;text-align:center;font-size:31px;font-weight:600;color:var(--black)}

/* header */
.topbar{position:absolute;top:0;left:0;width:1200px;height:83px;background:var(--black)}
.brand{position:absolute;left:62px;top:26px;color:var(--white);font-size:23px;font-weight:600}
.search{position:absolute;left:641px;top:24px;width:203px;height:36px;border-bottom:1px solid #777;color:#999;font-size:12px;padding-top:4px}
.search svg{position:absolute;right:4px;top:6px}
.login{position:absolute;left:876px;top:19px;width:113px;height:41px;border:1.5px solid var(--white);color:var(--white);font-size:13px;font-weight:500;display:flex;align-items:center;justify-content:center}
.register{position:absolute;left:1003px;top:19px;width:135px;height:41px}
.navbar{position:absolute;top:83px;left:0;width:1200px;height:36px;background:var(--red);color:var(--white);font-size:13px}
.navbar span{position:absolute;top:9px}
.navbar .home{color:#ffd54a}
.navbar .buy{color:#ffd54a;font-weight:600;display:flex;align-items:center;gap:6px;top:8px}

/* hero */
.hero{position:absolute;top:119px;left:0;width:1200px;height:555px;background:linear-gradient(90deg,#141414 0%,#2a2624 40%,#4a2a26 62%,#3a1d1b 80%,#171615 100%)}
.hero-photo{position:absolute;left:430px;top:120px;width:700px;height:360px;background:radial-gradient(ellipse at 55% 55%,#b3201f 0%,#6a1414 40%,rgba(40,20,20,0) 72%)}
.hero-title{position:absolute;left:60px;top:112px;color:var(--red);font-size:50px;font-weight:600;line-height:1.1}
.hero-title span{display:block;color:var(--white);font-size:38px;font-weight:400}
.hero-text{position:absolute;left:62px;top:264px;width:362px;color:var(--white);font-size:13px;line-height:23px}
.hero .btn{position:absolute;left:60px;top:387px;width:183px;height:39px}
.slide-count{position:absolute;left:1092px;top:478px;color:var(--white);font-size:30px;font-weight:500}
.slide-dots{position:absolute;left:1049px;top:525px;display:flex;gap:4px}
.slide-dots i{display:block;width:17px;height:4px;background:#8a8a8a}
.slide-dots i:first-child{background:var(--white)}

/* destinations */
.dest-card{position:absolute;top:822px;width:351px;height:438px;border:1px solid var(--line)}
.dest-card .photo{height:214px}
.dest-card h3{position:absolute;left:25px;top:237px;font-size:16px;font-weight:500}
.dest-card .date{position:absolute;left:25px;top:272px;font-size:12px;color:var(--muted);display:flex;align-items:center;gap:8px}
.dest-card p{position:absolute;left:25px;top:296px;width:235px;font-size:12px;line-height:21px;color:var(--muted)}
.dest-card .btn{position:absolute;left:24px;top:371px;width:182px;height:41px}

/* about */
.about{position:absolute;top:1335px;left:0;width:1200px;height:468px;background:linear-gradient(90deg,#1a1a1a 0%,#3b2a22 25%,#2a201c 45%,#0e0e0e 62%,#050505 100%)}
.about-photo{position:absolute;left:120px;top:70px;width:560px;height:340px;background:radial-gradient(ellipse at 50% 50%,#8e3518 0%,#4a2014 40%,rgba(20,14,12,0) 70%)}
.about h2{position:absolute;left:767px;top:70px;color:var(--white);font-size:30px;font-weight:600}
.about p{position:absolute;left:767px;width:375px;color:#e6e6e6;font-size:12px;line-height:21px}
.about .btn{position:absolute;left:767px;top:352px;width:181px;height:41px}

/* tickets */
.ticket{position:absolute;top:1947px;width:258px;height:364px;text-align:center}
.ticket .photo{height:187px}
.ticket h3{margin-top:14px;font-size:16px;font-weight:500;line-height:24px}
.ticket .price{margin-top:8px;font-size:14px;color:#555}
.ticket .price b{font-weight:600;font-size:12px;color:var(--ink)}
.qty{margin-top:5px;display:flex;justify-content:center;align-items:center;gap:18px;font-size:14px}
.qty i{display:flex;width:18px;height:18px;border:1px solid #888;border-radius:50%;align-items:center;justify-content:center;font-style:normal;font-size:13px;color:#555;line-height:1}
.ticket .btn{position:absolute;left:0;bottom:0;width:258px;height:36px;font-size:14px}

/* mission */
.mission{position:absolute;top:2386px;left:0;width:1200px;height:420px;background:linear-gradient(180deg,#1d1d1d 0%,#2c2c2c 45%,#161616 100%)}
.mv{position:absolute;top:74px;width:440px;text-align:center;color:var(--white)}
.mv .icon{width:86px;height:86px;margin:0 auto;background:var(--red);border:3px solid #111;outline:2px solid var(--red);display:flex;align-items:center;justify-content:center}
.mv h3{margin-top:18px;font-size:30px;font-weight:600;letter-spacing:1px}
.mv p{margin:8px auto 0;max-width:372px;font-size:12px;line-height:21px;color:#e2e2e2}

/* services */
.service{position:absolute;top:2956px;width:349px;height:224px;background:var(--soft);text-align:center}
.service svg{margin-top:42px}
.service h3{margin-top:10px;font-size:17px;font-weight:600}
.service p{margin-top:8px;font-size:12px;color:var(--muted)}
.service .btn{position:absolute;left:98px;top:206px;width:153px;height:39px}

/* faq */
.faq{position:absolute;top:3276px;left:0;width:1200px;height:537px;background:linear-gradient(90deg,#262626 0%,#3a3a3a 50%,#2d2a26 75%,#1e1e1e 100%)}
.faq-photo{position:absolute;left:600px;top:110px;width:560px;height:360px;background:radial-gradient(ellipse at 50% 55%,#6a2a22 0%,#3b2420 45%,rgba(40,36,32,0) 72%)}
.faq h2{position:absolute;left:62px;top:68px;color:var(--white);font-size:30px;font-weight:600}
.faq-item{position:absolute;left:60px;width:547px;border:1px solid #555;color:var(--white);font-size:14px;padding:0 24px;display:flex;align-items:center;justify-content:space-between}
.faq-item.open{background:var(--red);border-color:var(--red);display:block;padding-top:12px}
.faq-item.open .q{display:flex;justify-content:space-between;font-size:15px}
.faq-item.open p{margin-top:10px;padding-left:19px;width:400px;font-size:12px;line-height:22px}

/* testimonials */
.review{position:absolute;top:3960px;width:349px;height:235px;border:1px solid var(--line);padding:22px 25px}
.review p{font-size:12px;line-height:23px;color:#555}
.review .who{position:absolute;left:25px;top:158px;display:flex;align-items:center;gap:16px}
.review .avatar{width:54px;height:54px;background:linear-gradient(135deg,#5a4a3e,#9a8676)}
.review .stars{display:flex;gap:4px}
.review .name{font-size:13px;margin-top:4px}

/* vip */
.vip{position:absolute;top:4270px;left:0;width:1200px;height:399px;background:var(--soft)}
.vip-photo{position:absolute;left:601px;top:0;width:599px;height:399px;background:linear-gradient(135deg,#3a4d70 0%,#2a3145 45%,#5a3e3a 75%,#1f2a44 100%)}
.vip h2{position:absolute;left:62px;top:74px;font-size:31px;font-weight:600;letter-spacing:.5px}
.vip ul{position:absolute;left:62px;top:134px;list-style:none}
.vip li{font-size:14px;line-height:31px;display:flex;align-items:center;gap:12px}
.vip li::before{content:"";width:11px;height:11px;background:var(--red)}
.vip .price{position:absolute;left:62px;top:234px;font-size:17px;font-weight:600}
.vip .btn{position:absolute;left:60px;top:285px;width:154px;height:37px}

/* footer */
.footer{position:absolute;top:4669px;left:0;width:1200px;height:294px;background:var(--black);color:var(--white);text-align:center}
.footer h2{margin-top:46px;color:var(--red);font-size:40px;font-weight:600}
.footer p{width:480px;margin:14px auto 0;font-size:12px;line-height:22px}
.footer nav{margin-top:16px;font-size:11px;display:flex;justify-content:center;gap:18px}
.footer small{position:absolute;left:0;width:1200px;top:270px;font-size:11px;color:#ccc}
.chat{position:absolute;left:1070px;top:225px}
</style>
</head>
<body>

<header class="topbar">
  <div class="brand">Kestrel Voyages Elite</div>
  <div class="search">Search
    <svg width="14" height="14" viewBox="0 0 14 14" fill="none" stroke="#aaa" stroke-width="1.5"><circle cx="6" cy="6" r="4.5"/><path d="M9.5 9.5 13 13"/></svg>
  </div>
  <a class="login">LOGIN</a>
  <a class="btn register">REGISTER</a>
</header>
<nav class="navbar">
  <span class="home" style="left:62px">Home</span>
  <span style="left:154px">Destinations</span>
  <span style="left:289px">Packages</span>
  <span style="left:406px">About</span>
  <span style="left:499px">Contact Us</span>
  <span class="buy" style="left:957px"><svg width="14" height="14" viewBox="0 0 14 14" fill="#ffd54a"><path d="M8 0 2 8h4l-1 6 6-8H7z"/></svg>BUY TICKETS</span>
  <span style="left:1088px;font-weight:600">EN</span>
  <span style="left:1110px;opacity:.8">|</span>
  <span style="left:1125px">FR</span>
</nav>

<section class="hero">
  <div class="hero-photo" role="img" aria-label="Red race car speeding along a circuit at dusk"></div>
  <h1 class="hero-title">Kestrel Voyages<span>Elite</span></h1>
  <p class="hero-text">Discover the thrill of Torque League in the world's most iconic cities. Each destination offers exclusive race packages, luxury hospitality, and unforgettable cultural experiences.</p>
  <a class="btn">EXPLORE PACKAGES</a>
  <div class="slide-count">1/5</div>
  <div class="slide-dots"><i></i><i></i><i></i><i></i><i></i></div>
</section>

<h2 class="section-title" style="top:745px">Featured Destinations</h2>

<article class="dest-card" style="left:60px">
  <div class="photo" role="img" aria-label="Harbour-side grandstands with a race car on track" style="background:linear-gradient(180deg,#8fa3b6 0%,#6c6a5c 45%,#3a3c40 100%)"></div>
  <h3>Port Valmere Grand Prix</h3>
  <div class="date"><svg width="12" height="12" viewBox="0 0 12 12" fill="none" stroke="#777"><rect x="1" y="2" width="10" height="9"/><path d="M1 5h10"/></svg>May 22–25, 2025</div>
  <p>Witness the world's most glamorous race from trackside terraces and superyachts.</p>
  <a class="btn">VIEW PACKAGES <svg width="12" height="12" viewBox="0 0 12 12" fill="none" stroke="#fff" stroke-width="1.6"><path d="M2 10 10 2M4 2h6v6"/></svg></a>
</article>
<article class="dest-card" style="left:425px">
  <div class="photo" role="img" aria-label="Green race car leaving the pit lane" style="background:linear-gradient(180deg,#b9bcc0 0%,#5d6266 45%,#2e3436 100%)"></div>
  <h3>Sahrim Bay Grand Prix</h3>
  <div class="date"><svg width="12" height="12" viewBox="0 0 12 12" fill="none" stroke="#777"><rect x="1" y="2" width="10" height="9"/><path d="M1 5h10"/></svg>Dec 5–7, 2025</div>
  <p>A spectacular season finale under the lights — luxury meets adrenaline.</p>
  <a class="btn">VIEW PACKAGES <svg width="12" height="12" viewBox="0 0 12 12" fill="none" stroke="#fff" stroke-width="1.6"><path d="M2 10 10 2M4 2h6v6"/></svg></a>
</article>
<article class="dest-card" style="left:790px">
  <div class="photo" role="img" aria-label="City neon lights and an illuminated dome at night" style="background:linear-gradient(160deg,#1b1640 0%,#6a1f7a 40%,#c23a52 65%,#1a4f7a 100%)"></div>
  <h3>Nevora Strip Grand Prix</h3>
  <div class="date"><svg width="12" height="12" viewBox="0 0 12 12" fill="none" stroke="#777"><rect x="1" y="2" width="10" height="9"/><path d="M1 5h10"/></svg>Nov 20–23, 2025</div>
  <p>Experience the newest and most electric race weekend on the TL calendar.</p>
  <a class="btn">VIEW PACKAGES <svg width="12" height="12" viewBox="0 0 12 12" fill="none" stroke="#fff" stroke-width="1.6"><path d="M2 10 10 2M4 2h6v6"/></svg></a>
</article>

<section class="about">
  <div class="about-photo" role="img" aria-label="Orange race car in motion blur on a dark track"></div>
  <h2>About Kestrel Voyages</h2>
  <p style="top:134px">Lorem Ipsum has been the industry's standard dummy text ever since the 1500s, when an unknown printer took a galley of type and scrambled it to make a type specimen book. It has survived not only five centuries, but also the leap into electronic typesetting.</p>
  <p style="top:246px">Lorem Ipsum has been the industry's standard dummy text ever since the 1500s, when an unknown printer took a galley of type and scrambled it to make a type specimen book.</p>
  <a class="btn">EXPLORE PACKAGES</a>
</section>

<h2 class="section-title" style="top:1873px">Available Ticket</h2>

<article class="ticket" style="left:60px">
  <div class="photo" role="img" aria-label="Grandstand crowd under fireworks at night" style="background:linear-gradient(180deg,#0f1a3a 0%,#5a1a2a 55%,#b02a2a 100%)"></div>
  <h3>Brouwer Silver Main<br>Grandstand 3-Days</h3>
  <div class="price">€1.769,01 <b>EUR</b></div>
  <div class="qty"><i>−</i>0<i>+</i></div>
  <a class="btn">ADD TO CARD</a>
</article>
<article class="ticket" style="left:333px">
  <div class="photo" role="img" aria-label="Race start grid seen from a packed grandstand" style="background:linear-gradient(180deg,#7e9bc0 0%,#6f8a5e 45%,#6a6660 100%)"></div>
  <h3>Marcus Vale<br>Grandstand 3-Days</h3>
  <div class="price">€985,59 <b>EUR</b></div>
  <div class="qty"><i>−</i>0<i>+</i></div>
  <a class="btn">ADD TO CARD</a>
</article>
<article class="ticket" style="left:607px">
  <div class="photo" role="img" aria-label="Race cars cornering on a street circuit" style="background:linear-gradient(180deg,#9aa3ad 0%,#7e8a80 45%,#4a4e56 100%)"></div>
  <h3>Nova Sphere<br>Grandstands 3-Days</h3>
  <div class="price">€1.213,03 <b>EUR</b></div>
  <div class="qty"><i>−</i>0<i>+</i></div>
  <a class="btn">ADD TO CARD</a>
</article>
<article class="ticket" style="left:880px">
  <div class="photo" role="img" aria-label="Drivers celebrating on a podium with flags behind" style="background:linear-gradient(180deg,#b23030 0%,#3e4a7a 45%,#2a7a8a 100%)"></div>
  <h3>Nova Sphere<br>Grandstands Middle Rows</h3>
  <div class="price">€1.288,85 <b>EUR</b></div>
  <div class="qty"><i>−</i>0<i>+</i></div>
  <a class="btn">ADD TO CARD</a>
</article>

<section class="mission" role="img" aria-label="Race cars on a wet track in dim light">
  <div class="mv" style="left:102px">
    <div class="icon"><svg width="46" height="46" viewBox="0 0 46 46" fill="none" stroke="#fff" stroke-width="2"><circle cx="21" cy="25" r="16"/><circle cx="21" cy="25" r="9"/><circle cx="21" cy="25" r="2"/><path d="M21 25 38 8M32 8h6v6"/></svg></div>
    <h3>MISSION</h3>
    <p>That's why we craft once-in-a-lifetime Torque League journeys — where the roar of the engines meets the soul of the city. Where luxury travel and local culture collide with pure adrenaline. Where you don't just watch the race… you become part of its story.</p>
  </div>
  <div class="mv" style="left:656px">
    <div class="icon"><svg width="46" height="46" viewBox="0 0 46 46" fill="none" stroke="#fff" stroke-width="2"><path d="M4 23c5-8 11-12 19-12s14 4 19 12c-5 8-11 12-19 12S9 31 4 23z"/><circle cx="23" cy="23" r="6"/><path d="M23 4v4M23 38v4M8 8l3 3M38 8l-3 3"/></svg></div>
    <h3>VISION</h3>
    <p>We believe life is meant to be lived at full throttle.<br>Not just seen, but felt. Not just remembered, but relived again and again.</p>
  </div>
</section>

<h2 class="section-title" style="top:2877px">OUR SERVICES</h2>

<article class="service" style="left:60px">
  <svg width="62" height="60" viewBox="0 0 62 60" fill="none" stroke="#e31e24" stroke-width="2"><rect x="8" y="8" width="44" height="32"/><path d="M2 46h56v5H2zM14 16h14M14 22h20M14 28h16"/><circle cx="48" cy="12" r="9" fill="#f1f1f1"/><path d="M44 12h8M48 8l3 4-3 4"/></svg>
  <h3>Flight Booking Service</h3>
  <p>Integrates with global flight providers</p>
  <a class="btn">BOOKING NOW</a>
</article>
<article class="service" style="left:425px">
  <svg width="62" height="60" viewBox="0 0 62 60" fill="none" stroke="#e31e24" stroke-width="2"><rect x="12" y="6" width="26" height="50"/><path d="M18 14h4M28 14h4M18 22h4M28 22h4M18 30h4M28 30h4M22 56v-9h6v9"/><rect x="38" y="30" width="16" height="26"/><path d="M43 38h6M43 45h6"/></svg>
  <h3>Hotel Booking Service</h3>
  <p>Connects to hotel aggregator APIs.</p>
  <a class="btn">BOOKING NOW</a>
</article>
<article class="service" style="left:790px">
  <svg width="62" height="60" viewBox="0 0 62 60" fill="none" stroke="#e31e24" stroke-width="2"><path d="M6 10h50v12a5 5 0 0 0 0 10v12H6V32a5 5 0 0 0 0-10z"/><path d="M40 10v34" stroke-dasharray="3 3"/><path d="M14 20h18M14 27h14M14 34h16"/></svg>
  <h3>Ticket Booking Service</h3>
  <p>Manages TL race ticket inventory.</p>
  <a class="btn">BOOKING NOW</a>
</article>

<section class="faq">
  <div class="faq-photo" role="img" aria-label="Red and black sports race car on a wet track"></div>
  <h2>FREQUENTLY ASKED QUESTIONS</h2>
  <div class="faq-item" style="top:145px;height:46px"><span>1. What is included in an TL travel package?</span><span>+</span></div>
  <div class="faq-item open" style="top:206px;height:129px">
    <div class="q"><span>2. Can I book just race tickets without flights or hotels?</span><span>−</span></div>
    <p>Yes. You can purchase race tickets only if you already have your own travel plans. Simply select "Tickets Only" during checkout.</p>
  </div>
  <div class="faq-item" style="top:351px;height:46px"><span>3. Are flights included in every package?</span><span>+</span></div>
  <div class="faq-item" style="top:414px;height:47px"><span>4. How do I know my booking is confirmed?</span><span>+</span></div>
</section>

<h2 class="section-title" style="top:3884px">TESTIMONIAL</h2>

<article class="review" style="left:60px">
  <p>Lorem Ipsum has been the industry's standard dummy text ever since the 1500s, when an unknown printer took a galley of type and scrambled it to make a type specimen book.</p>
  <div class="who"><div class="avatar" role="img" aria-label="Client portrait"></div><div><div class="stars"><svg width="96" height="16" viewBox="0 0 96 16" fill="#f5b301"><path id="s" d="M8 0l2.4 5 5.6.6-4.2 3.8 1.2 5.6L8 12.2 3 15l1.2-5.6L0 5.6 5.6 5z"/><use href="#s" x="20"/><use href="#s" x="40"/><use href="#s" x="60"/><use href="#s" x="80"/></svg></div><div class="name">- Client Name</div></div></div>
</article>
<article class="review" style="left:425px">
  <p>Lorem Ipsum has been the industry's standard dummy text ever since the 1500s, when an unknown printer took a galley of type and scrambled it to make a type specimen book.</p>
  <div class="who"><div class="avatar" role="img" aria-label="Client portrait"></div><div><div class="stars"><svg width="96" height="16" viewBox="0 0 96 16" fill="#f5b301"><use href="#s"/><use href="#s" x="20"/><use href="#s" x="40"/><use href="#s" x="60"/><use href="#s" x="80"/></svg></div><div class="name">- Client Name</div></div></div>
</article>
<article class="review" style="left:790px">
  <p>Lorem Ipsum has been the industry's standard dummy text ever since the 1500s, when an unknown printer took a galley of type and scrambled it to make a type specimen book.</p>
  <div class="who"><div class="avatar" role="img" aria-label="Client portrait"></div><div><div class="stars"><svg width="96" height="16" viewBox="0 0 96 16" fill="#f5b301"><use href="#s"/><use href="#s" x="20"/><use href="#s" x="40"/><use href="#s" x="60"/><use href="#s" x="80"/></svg></div><div class="name">- Client Name</div></div></div>
</article>

<section class="vip">
  <h2>VIP TERRACE EXPERIENCE</h2>
  <ul>
    <li>Trackside terrace view at Harbour Square</li>
    <li>Full-day gourmet catering &amp; champagne bar</li>
    <li>Exclusive access to VIP areas</li>
  </ul>
  <div class="price">€4,250 per person</div>
  <a class="btn">BOOKING NOW</a>
  <div class="vip-photo" role="img" aria-label="Guests seated in a VIP hospitality terrace"></div>
</section>

<footer class="footer">
  <h2>Kestrel Voyages Elite</h2>
  <p>Discover the thrill of Torque League in the world's most iconic cities. Each destination offers exclusive race packages, luxury hospitality, and unforgettable cultural experiences.</p>
  <nav><a>Home</a><span>|</span><a>Destinations</a><span>|</span><a>Packages</a><span>|</span><a>About Us</a><span>|</span><a>Contact Us</a></nav>
  <svg class="chat" width="50" height="44" viewBox="0 0 50 44" fill="#e31e24"><path d="M6 4h28a4 4 0 0 1 4 4v16a4 4 0 0 1-4 4H16l-8 7v-7H6a4 4 0 0 1-4-4V8a4 4 0 0 1 4-4z"/><path d="M40 14h4a4 4 0 0 1 4 4v12a4 4 0 0 1-4 4h-2v6l-7-6H24a4 4 0 0 1-4-4v-2h14a6 6 0 0 0 6-6z"/><circle cx="12" cy="16" r="2" fill="#fff"/><circle cx="20" cy="16" r="2" fill="#fff"/><circle cx="28" cy="16" r="2" fill="#fff"/></svg>
  <small>© 2025 Kestrel Voyages Elite – All Rights Reserved</small>
</footer>

</body>
</html>
```